Clean and modern business cards

Looking for an updated business card design for my dental office “corvanta dental” . Looking for a modern clean / sleek design . I’m thinking black background but open to seeing other options . One side needs to have an appointment card . Card needs to have logo, dentist name , phone, email , address . I’ve attached couple of cards I thought were cool as well as my logo
Target Market(s)
Dental patients
Industry/Entity Type
Dentistry
Contact Information for Business Card
Phone email address

```html
<!DOCTYPE html>
<html lang="en">
<head>
<meta charset="utf-8">
<title>Corvanta Dental – Business Card</title>
<link href="https://fonts.googleapis.com/css2?family=Montserrat:wght@400;500;600;700&display=swap" rel="stylesheet">
<style>
  :root {
    --stage: #2b2b2d;
    --card-dark: #1c1c1e;
    --card-light: #ffffff;
    --ink: #141414;
    --rule: #c9c9c9;
    --teal: #1b8a9a;
    --purple: #5a3a8e;
    --gold: #d2a632;
  }
  * { margin: 0; padding: 0; box-sizing: border-box; }
  html, body { width: 1200px; height: 1108px; overflow: hidden; }
  body {
    background: var(--stage);
    font-family: "Montserrat", sans-serif;
    display: flex;
    align-items: center;
    justify-content: center;
    gap: 60px;
  }
  .card {
    width: 420px;
    height: 735px;
    border-radius: 3px;
    overflow: hidden;
    position: relative;
    box-shadow: 0 18px 40px rgba(0,0,0,.45);
  }

  /* Front */
  .card--front { background: var(--card-dark); }
  .front__brand {
    position: absolute;
    top: 96px;
    left: 0; right: 0;
    text-align: center;
    color: #fff;
    font-weight: 700;
    font-size: 30px;
    letter-spacing: 2px;
    text-transform: uppercase;
    line-height: 1.3;
  }
  .front__art {
    position: absolute;
    left: 0; right: 0;
    top: 250px;
    bottom: 0;
    background: linear-gradient(180deg, var(--card-dark) 0%, var(--teal) 35%, var(--purple) 100%);
  }

  /* Back */
  .card--back {
    background: var(--card-light);
    color: var(--ink);
    padding: 84px 48px 0;
    display: flex;
    flex-direction: column;
  }
  .appt__title {
    font-size: 22px;
    font-weight: 400;
    text-align: center;
    margin-bottom: 22px;
  }
  .appt__field {
    font-size: 18px;
    border-bottom: 1px solid var(--rule);
    padding: 18px 0 10px;
  }
  .appt__notice {
    font-size: 13px;
    line-height: 1.4;
    text-align: center;
    margin-top: 40px;
  }
  .contact {
    margin-top: 56px;
    text-align: center;
    font-size: 17px;
    line-height: 1.6;
  }
  .contact__name {
    font-size: 23px;
    font-weight: 600;
    text-transform: uppercase;
    letter-spacing: 0.5px;
    margin-bottom: 8px;
  }
  .back__brand {
    margin-top: auto;
    margin-bottom: 70px;
    display: flex;
    align-items: center;
    justify-content: center;
    gap: 14px;
    font-weight: 700;
    font-size: 20px;
    letter-spacing: 1.5px;
    text-transform: uppercase;
    white-space: nowrap;
  }
  .back__brand-dot {
    width: 40px; height: 40px;
    flex: 0 0 40px;
    border-radius: 50%;
    background: var(--teal);
  }
</style>
</head>
<body>
  <section class="card card--front">
    <div class="front__brand">Corvanta<br>Dental</div>
    <div class="front__art" role="img" aria-label="Colourful dental brand illustration"></div>
  </section>

  <section class="card card--back">
    <h2 class="appt__title">Your Next Appointment is:</h2>
    <div class="appt__field">Date:</div>
    <div class="appt__field">Time:</div>
    <p class="appt__notice">To Cancel Or Reschedule Please<br>Notify Us At Least 48 Hours<br>Prior To Your Scheduled Appointment</p>

    <div class="contact">
      <p class="contact__name">Dr. Elias Varnek</p>
      <p>(204) 555-01 47</p>
      <p>1620 Larkspur Ave, Winnipeg, MB</p>
      <p>corvantadental.ca</p>
      <p>contact@corvantadental.ca</p>
    </div>

    <div class="back__brand">
      <span class="back__brand-dot"></span>
      <span>Corvanta Dental</span>
    </div>
  </section>
</body>
</html>
```